Corvallin Property Solutions need a business card design

Hello guys. We would need a business card design asap please.
We are a start up property investment business based in London UK specialised in buying, selling, managing and letting properties and helping distressed property owners.
The name of our Business is Corvallin, the logo symbolises the four fundamental elements of the world (earth, air, fire and water) and so it stands for strength, stability, longevity.
We would like the business card to communicate professionalism and reliability. Many many thanks indeed for your work.

Details:

1.) Marisol Dunkley
Property Investor
Mobile: +44(0)7700362517
Email: marisol.corvallin@quilbrook.example

2.) Tomas Brindle
Property Investor
Mobile: +44(0)7700845926
Email: tomas.corvallin@quilbrook.example

Industry/Entity Type

Investment

```html
<!DOCTYPE html>
<html lang="en">
<head>
<meta charset="utf-8">
<title>Corvallin Property Solutions – Business Card</title>
<link href="https://fonts.googleapis.com/css2?family=Josefin+Sans:wght@700&family=Raleway:wght@300;400&display=swap" rel="stylesheet">
<style>
  :root {
    --page-bg: #e4e2de;
    --card-bg: #f1f1f0;
    --ink: #1c1c1c;
    --ink-soft: #3a3a3a;
    --accent-red: #c8202e;
    --brand-mark: #d9d9d7;
    --card-shadow: rgba(0, 0, 0, 0.18);
  }
  * { margin: 0; padding: 0; box-sizing: border-box; }
  html, body {
    width: 1200px;
    height: 900px;
    overflow: hidden;
    background: var(--page-bg);
  }
  .sheet {
    width: 1200px;
    height: 900px;
    display: flex;
    flex-direction: column;
    align-items: center;
    justify-content: center;
    gap: 60px;
  }
  .card {
    position: relative;
    width: 630px;
    height: 360px;
    background: var(--card-bg);
    box-shadow: 0 8px 24px var(--card-shadow);
    overflow: hidden;
  }

  /* Brand side */
  .card--brand {
    display: flex;
    align-items: center;
    justify-content: center;
  }
  .brand-lockup {
    display: flex;
    flex-direction: column;
    align-items: flex-start;
  }
  .brand-name {
    font-family: "Josefin Sans", sans-serif;
    font-weight: 700;
    font-size: 46px;
    letter-spacing: 3px;
    color: var(--ink);
    line-height: 1;
  }
  .brand-tagline {
    font-family: "Josefin Sans", sans-serif;
    font-weight: 700;
    font-size: 15px;
    letter-spacing: 1.5px;
    color: var(--ink);
    margin-top: 8px;
    padding-left: 2px;
  }

  /* Contact side */
  .card--contact { padding: 48px 0 0 48px; }
  .person-name {
    font-family: "Raleway", sans-serif;
    font-weight: 300;
    font-size: 27px;
    letter-spacing: 1.5px;
    color: var(--ink-soft);
    line-height: 1.1;
  }
  .person-role {
    font-family: "Raleway", sans-serif;
    font-weight: 400;
    font-size: 15px;
    color: var(--ink-soft);
    margin-top: 4px;
  }
  .divider {
    width: 290px;
    height: 1.5px;
    background: var(--accent-red);
    margin: 18px 0 30px;
  }
  .contact-item { margin-bottom: 22px; }
  .contact-label {
    font-family: "Raleway", sans-serif;
    font-weight: 400;
    font-size: 14px;
    letter-spacing: 0.5px;
    color: var(--accent-red);
    text-transform: uppercase;
  }
  .contact-value {
    font-family: "Raleway", sans-serif;
    font-weight: 400;
    font-size: 15px;
    color: var(--ink);
    margin-top: 2px;
  }
  .brand-watermark {
    position: absolute;
    right: 34px;
    bottom: 30px;
    font-family: "Josefin Sans", sans-serif;
    font-weight: 700;
    font-size: 64px;
    letter-spacing: 3px;
    color: var(--brand-mark);
    line-height: 1;
  }
</style>
</head>
<body>
  <main class="sheet">
    <section class="card card--brand" aria-label="Card front">
      <div class="brand-lockup">
        <div class="brand-name">CORVALLIN</div>
        <div class="brand-tagline">PROPERTY SOLUTIONS</div>
      </div>
    </section>

    <section class="card card--contact" aria-label="Card back">
      <h1 class="person-name">MARISOL DUNKLEY</h1>
      <p class="person-role">Property Investor</p>
      <div class="divider"></div>
      <div class="contact-item">
        <div class="contact-label">Mobile</div>
        <div class="contact-value">+44(0)7700362517</div>
      </div>
      <div class="contact-item">
        <div class="contact-label">Email</div>
        <div class="contact-value">marisol.corvallin@quilbrook.example</div>
      </div>
      <div class="brand-watermark">CORVALLIN</div>
    </section>
  </main>
</body>
</html>
```